Business card design needed

I need a business card for my new Food & Lifestyle Coaching business - "Bloomvale Food & Lifestlye Coaching"

i already have a logo and would like to have that incorporated into the business card, obviously.

i would like a design that says "fresh" and "funky" - my target market is female, aged 20-45 so i want something that will stand out to them when they see it.

My "Company Colour" is Apple Green
Updates

Thankyou to everyone who has submitted a design for my project. At this stage i have quite a large number of designs to chose from and with only a short time until my project closes i am focusing now on chosing from those i have already shortlisted so am unfortunately not considering any new desings.

Thankyou again for your interest in my project.

Target Market(s)

Female, Health Conscious (or looking to improve their health/lifestyle), aged between 20-45

Industry/Entity Type

Business

Contact Information for Business Card

Tamsin Corley
Ph: 0417382946
Email: eatwell@marovex.com

Requirements
Must have
• Must include my existing Logo
Nice to have
• Would be nice to incoirporate and appointment card on the back

```html
<!DOCTYPE html>
<html lang="en">
<head>
<meta charset="utf-8">
<title>Bloomvale Business &amp; Appointment Card</title>
<link href="https://fonts.googleapis.com/css2?family=Quicksand:wght@400;500&display=swap" rel="stylesheet">
<style>
  :root {
    --apple-green: #8cc63f;
    --apple-green-soft: #b7dc85;
    --ink: #231f20;
    --white: #ffffff;
    --backdrop: #efece7;
    --rule: rgba(255,255,255,0.75);
  }
  * { margin: 0; padding: 0; box-sizing: border-box; }
  html, body { width: 1200px; height: 1200px; overflow: hidden; }
  body {
    background: var(--backdrop);
    font-family: "Quicksand", sans-serif;
    position: relative;
  }
  .card {
    position: absolute;
    background: var(--white);
    overflow: hidden;
    box-shadow: 0 2px 8px rgba(0,0,0,0.18);
  }

  /* Front */
  .card--front { left: 31px; top: 24px; width: 852px; height: 530px; }
  .brand__dot {
    position: absolute; left: 92px; top: 118px;
    width: 150px; height: 150px; border-radius: 50%;
    background: var(--apple-green);
  }
  .brand__title {
    position: absolute; left: 268px; top: 92px;
    font-size: 100px; font-weight: 500; line-height: 1; letter-spacing: -2px;
    color: var(--ink);
  }
  .brand__tagline {
    position: absolute; right: 124px; top: 298px;
    font-size: 25px; font-weight: 500; color: var(--ink);
  }
  .contact-band {
    position: absolute; left: 0; bottom: 0; width: 100%; height: 137px;
    background: var(--apple-green); color: var(--white);
    text-align: center; padding-top: 14px;
  }
  .contact-band__name {
    font-size: 42px; font-weight: 400; letter-spacing: 1px; line-height: 1.05;
    display: flex; align-items: center; justify-content: center; gap: 14px;
  }
  .contact-band__divider { width: 12px; height: 12px; border-radius: 50%; background: var(--white); }
  .contact-band__line { font-size: 25px; line-height: 1.45; }
  .contact-band__label { font-weight: 500; }

  /* Back */
  .card--back { left: 329px; top: 620px; width: 857px; height: 529px; }
  .motif {
    position: absolute; left: 0; top: 0; width: 405px; height: 100%;
    background:
      radial-gradient(ellipse 70% 45% at 62% 28%, var(--apple-green) 0%, var(--apple-green) 55%, transparent 72%),
      radial-gradient(ellipse 60% 40% at 30% 78%, var(--apple-green) 0%, var(--apple-green) 50%, transparent 70%),
      linear-gradient(135deg, var(--white) 0%, var(--apple-green-soft) 100%);
  }
  .appointment {
    position: absolute; right: 0; top: 0; width: 452px; height: 100%;
    background: var(--apple-green); color: var(--white);
  }
  .appointment__heading {
    position: absolute; left: 28px; top: 14px;
    font-size: 30px; font-weight: 400; letter-spacing: 0.5px;
  }
  .appointment__wave { position: absolute; left: 0; top: 60px; }
  .appointment__field {
    position: absolute; left: 38px; right: 26px;
    display: flex; align-items: baseline; gap: 10px; font-size: 25px;
  }
  .appointment__field--date { top: 118px; }
  .appointment__field--time { top: 185px; }
  .appointment__blank { flex: 1; border-bottom: 2px dotted var(--rule); height: 22px; }
  .back-brand {
    position: absolute; right: 26px; bottom: 28px; color: var(--white);
    display: flex; align-items: center; gap: 10px; font-weight: 500; line-height: 1;
  }
  .back-brand__dot { width: 30px; height: 30px; border-radius: 50%; background: var(--white); }
  .back-brand__title { display: block; font-size: 40px; }
  .back-brand__tagline { display: block; font-size: 11px; margin-top: 4px; text-align: right; }
</style>
</head>
<body>
  <section class="card card--front" aria-label="Business card front">
    <span class="brand__dot"></span>
    <p class="brand__title">Bloomvale</p>
    <p class="brand__tagline">Food &amp; Lifestlye Coaching</p>
    <div class="contact-band">
      <p class="contact-band__name">TAMSIN<span class="contact-band__divider"></span>CORLEY</p>
      <p class="contact-band__line"><span class="contact-band__label">Ph:</span> 0417382946</p>
      <p class="contact-band__line"><span class="contact-band__label">Email:</span> eatwell@marovex.com</p>
    </div>
  </section>

  <section class="card card--back" aria-label="Appointment card back">
    <div class="motif" role="img" aria-label="Large apple-green leaf motif decoration"></div>
    <div class="appointment">
      <h2 class="appointment__heading">OUR NEXT APPOINTMENT</h2>
      <svg class="appointment__wave" width="452" height="24" viewBox="0 0 452 24">
        <path d="M0 14 C60 4 120 20 200 12 S340 4 452 10" fill="none" stroke="#ffffff" stroke-width="3" stroke-dasharray="2 6" stroke-linecap="round"/>
      </svg>
      <div class="appointment__field appointment__field--date"><span>Date:</span><span class="appointment__blank"></span></div>
      <div class="appointment__field appointment__field--time"><span>Time:</span><span class="appointment__blank"></span></div>
      <div class="back-brand">
        <span class="back-brand__dot"></span>
        <p>
          <span class="back-brand__title">Bloomvale</span>
          <span class="back-brand__tagline">Food &amp; Lifestlye Coaching</span>
        </p>
      </div>
    </div>
  </section>
</body>
</html>
```